*no text if possible, unless absolutely necessary
need infographic
we are needing infographic icons to represent the following: (one of the following per icon image) note: these will be used to describe the features of performance apparel fabrics - breathability - moisture wicking - pre-shrunk - 4-way stretch - antimicrobial (anti stink) - anti pill - compression - quality/durability - guarantee
PondwickTamble PondwickTamble
now unveiled
dalemurtagh dalemurtagh
PondwickTamble: We are not able to see each others entries; the only entries we can view are our own. 4, 5, & 6 are showed as "VIELED PROJECT".
Thanks to all who have submitted entries. To offer feedback for future submissions, we like the look of the more graphic nature of entries 4,5,&6.
PondwickTamble, Do you have any sort of feedback on the other designs that were submitted? I see you rated one designers projects, but nobody else's has any stars. We'd appreciate any and all feedback based on the work we've done for you.

```html
<!DOCTYPE html>
<html lang="en">
<head>
<meta charset="utf-8">
<title>Performance Fabric Features</title>
<link rel="stylesheet" href="https://fonts.googleapis.com/css2?family=Open+Sans:wght@400;600&display=swap">
<style>
  :root {
    --brand-blue: #29aae1;
    --paper: #ffffff;
  }
  html, body {
    margin: 0;
    padding: 0;
    width: 1200px;
    height: 1085px;
    overflow: hidden;
    background: var(--paper);
  }
  .feature-sheet {
    display: block;
    width: 1200px;
    height: 1085px;
  }
  .feature-label {
    font-family: "Open Sans", Arial, sans-serif;
    fill: var(--brand-blue);
  }
  .feature-label--major { font-size: 17px; font-weight: 600; }
  .feature-label--minor { font-size: 13px; font-weight: 400; }
  .feature-label--mid { font-size: 14px; font-weight: 400; }
  .icon-fill { fill: var(--brand-blue); }
  .icon-stroke { fill: none; stroke: var(--brand-blue); }
  .icon-knockout { stroke: var(--paper); fill: none; }
</style>
</head>
<body>
<svg class="feature-sheet" viewBox="0 0 420 380" xmlns="http://www.w3.org/2000/svg" role="img" aria-label="Performance fabric feature list with icons">

  <!-- breathability -->
  <g class="icon icon-breathability">
    <circle class="icon-fill" cx="144" cy="88" r="8"/>
    <circle class="icon-fill" cx="161" cy="74.5" r="6"/>
    <circle class="icon-fill" cx="176" cy="64.5" r="4.5"/>
    <circle class="icon-fill" cx="190" cy="57.5" r="2.8"/>
  </g>
  <text class="feature-label feature-label--major" x="160" y="101">Breathability</text>

  <!-- moisture wicking -->
  <text class="feature-label feature-label--minor" x="161" y="128">moisture wicking</text>
  <path class="icon-fill icon-drop" d="M288 105 Q281 116 281 121 a7 7 0 0 0 14 0 Q295 116 288 105 Z"/>

  <!-- pre-shrunk -->
  <g class="icon icon-preshrunk">
    <rect class="icon-fill" x="142.5" y="145.5" width="5" height="5"/>
    <path class="icon-fill" d="M145 144 L140 138 H143 V136 H147 V138 H150 Z"/>
    <path class="icon-fill" d="M145 152 L140 158 H143 V160 H147 V158 H150 Z"/>
    <path class="icon-fill" d="M141 148 L135 143 V146 H133 V150 H135 V153 Z"/>
    <path class="icon-fill" d="M149 148 L155 143 V146 H157 V150 H155 V153 Z"/>
  </g>
  <text class="feature-label feature-label--major" x="158" y="154">pre-shrunk</text>

  <!-- 4-way stretch -->
  <text class="feature-label feature-label--minor" x="155" y="177">4-way stretch</text>
  <g class="icon icon-stretch">
    <path class="icon-stroke" stroke-width="3" d="M270 166 L282 178 M282 166 L270 178"/>
    <path class="icon-fill" d="M267 163 H273 L267 169 Z M285 163 V169 L279 163 Z M267 181 V175 L273 181 Z M285 181 H279 L285 175 Z"/>
  </g>

  <!-- antimicrobial -->
  <g class="icon icon-antimicrobial">
    <circle class="icon-stroke" stroke-width="1.6" cx="141" cy="201" r="10"/>
    <path class="icon-fill" d="M141 199 L137.5 195 H144.5 Z M141 203 L137.5 207 H144.5 Z M139 201 L135 197.5 V204.5 Z M143 201 L147 197.5 V204.5 Z"/>
  </g>
  <text class="feature-label feature-label--major" x="157" y="208">antimicrobial</text>

  <!-- anti pill -->
  <text class="feature-label feature-label--minor" x="159" y="231">anti pill</text>
  <g class="icon icon-antipill">
    <circle class="icon-fill" cx="228" cy="226" r="9"/>
    <path class="icon-knockout" stroke-width="1.4" d="M223 220 L233 232 M233 220 L223 232"/>
  </g>

  <!-- compression -->
  <g class="icon icon-compression">
    <path class="icon-stroke" stroke-width="2.2" d="M133 247 V257 M140 247 V257 M147 247 V257"/>
    <path class="icon-fill" d="M130 256 H136 L133 262 Z M137 256 H143 L140 262 Z M144 256 H150 L147 262 Z"/>
  </g>
  <text class="feature-label feature-label--mid" x="152" y="259">compression</text>

  <!-- quality / durability -->
  <text class="feature-label feature-label--minor" x="152" y="281">quality/durability</text>
  <g class="icon icon-durability">
    <circle class="icon-fill" cx="281" cy="274" r="10"/>
    <path class="icon-knockout" stroke-width="2.4" d="M276 277 A5.5 5.5 0 1 0 279 269"/>
    <path fill="#ffffff" d="M281 265 L277 270 L283 271.5 Z"/>
  </g>

  <!-- guarantee -->
  <g class="icon icon-guarantee">
    <path class="icon-fill" d="M124 298 L131 296 L137 299 L143 296 L149 299 L149 305 L144 310 L139 312 L133 307 L128 306 L124 305 Z"/>
    <path class="icon-knockout" stroke-width="1" d="M132 300 L138 305 M136 305 L140 309 M137 299 L143 303"/>
  </g>
  <text class="feature-label feature-label--major" x="153" y="306">guarantee</text>
</svg>
</body>
</html>
```